Wordpress Website for electrician

I'm looking for an easy to maintain website for my electrical contracting business. Need a professional and appealing site.
Im wanting a website where clients can come on and look at services we offer, case studies and advertise our services.
Colours I'm wanting to incorporate are green, white, black and grey
I'm wanting a big slide show on main page where I can place advertising etc.
Menu is to include home, services, our work, specials, energy efficiency and contact
My existing site is www.brivolelectric.com.au
looking for something with a similar layout to this website
Target Market(s)
Businesses
Industry/Entity Type
Electrician
Look and feel

```html
<!DOCTYPE html>
<html lang="en">
<head>
<meta charset="utf-8">
<title>Brivol Electric – Electrical Contractor</title>
<link href="https://fonts.googleapis.com/css2?family=Open+Sans:wght@400;600;700&family=Cuprum:wght@400&display=swap" rel="stylesheet">
<style>
  :root {
    --green: #2fa83a;
    --green-light: #45c24e;
    --green-dark: #16801f;
    --black: #0b0b0b;
    --ink: #1a1a1a;
    --grey: #777777;
    --grey-light: #d6d6d6;
    --white: #ffffff;
  }
  * { box-sizing: border-box; margin: 0; padding: 0; }
  html, body { width: 748px; height: 1200px; overflow: hidden; }
  body { position: relative; background: var(--white); font-family: "Open Sans", Arial, sans-serif; color: var(--ink); }

  .brand { position: absolute; left: 16px; top: 30px; display: flex; align-items: center; gap: 10px; }
  .brand-dot { width: 30px; height: 30px; border-radius: 50%; background: var(--green); }
  .brand-name { font-size: 28px; font-weight: 600; color: var(--green); letter-spacing: -0.5px; }

  .search { position: absolute; left: 565px; top: 35px; width: 171px; height: 22px; border: 1px solid #cfcfcf; display: flex; }
  .search-field { flex: 1; font-size: 11px; color: #999; padding: 3px 6px; }
  .search-button { width: 27px; border-left: 1px solid #cfcfcf; background: linear-gradient(#fafafa, #e4e4e4); display: flex; align-items: center; justify-content: center; }

  .main-nav { position: absolute; left: 0; top: 91px; width: 748px; height: 29px; background: linear-gradient(#3a3a3a, #050505); display: flex; }
  .main-nav a { display: flex; align-items: center; justify-content: center; color: var(--white); font-size: 11.5px; font-weight: 700; text-decoration: none; border-right: 1px solid #cfcfcf; }
  .main-nav a:last-child { border-right: none; }

  .hero { position: absolute; left: 0; top: 120px; width: 748px; height: 653px; background: linear-gradient(180deg, #f4f4f4 0%, #e8e6e4 45%, #b9b8b2 75%, #8a8d76 100%); }
  .hero-arrow { position: absolute; top: 270px; }
  .hero-arrow.prev { left: 12px; }
  .hero-arrow.next { right: 12px; }
  .hero-caption { position: absolute; left: 85px; top: 307px; width: 580px; height: 84px; background: rgba(255,255,255,0.75); text-align: center; font-family: "Cuprum", "Open Sans", sans-serif; font-size: 27px; line-height: 36px; color: #222; padding-top: 6px; letter-spacing: 0.5px; }

  .promo { position: absolute; top: 561px; height: 208px; border: 2px solid var(--white); box-shadow: 0 0 4px rgba(0,0,0,0.4); padding: 10px 12px; color: var(--white); }
  .promo-led { left: 12px; width: 343px; background: linear-gradient(#141414, #000); }
  .promo-energy { left: 383px; width: 352px; background: linear-gradient(#2aa034, #3dbb45 60%, #1d8b26); }
  .promo-title { font-family: "Cuprum", "Open Sans", sans-serif; font-size: 19.5px; font-weight: 400; letter-spacing: 1px; line-height: 27px; }
  .promo-text { font-size: 9.5px; line-height: 18px; margin-top: 6px; }
  .promo-led .promo-text { color: #6b6b6b; }
  .promo-energy .promo-text { color: #0d2e10; }
  .promo-actions { position: absolute; left: 12px; bottom: 14px; display: flex; gap: 16px; }
  .btn { display: inline-flex; align-items: center; justify-content: center; height: 28px; font-size: 12.5px; font-weight: 600; color: var(--white); text-decoration: none; border-radius: 3px; letter-spacing: 0.5px; }
  .btn-green { background: linear-gradient(var(--green-light), var(--green-dark)); border: 1px solid #8fe394; }
  .btn-dark { background: linear-gradient(#2a2a2a, #000); border: 1px solid #e5e5e5; }

  .rule { position: absolute; left: 12px; width: 724px; height: 1px; background: var(--grey-light); }

  .service { position: absolute; top: 803px; width: 205px; }
  .service-title { font-size: 18px; font-weight: 400; font-variant: small-caps; letter-spacing: 1px; color: var(--black); }
  .service-image { width: 198px; height: 108px; margin-top: 10px; box-shadow: 0 3px 3px rgba(0,0,0,0.25); }
  .service-text { font-size: 9.5px; line-height: 16px; color: var(--grey); margin-top: 14px; width: 200px; letter-spacing: 0.3px; }
  .btn-more { position: absolute; top: 242px; left: -2px; width: 102px; height: 26px; background: linear-gradient(#2d2d2d, #000); border-radius: 3px; color: var(--white); font-size: 10.5px; font-weight: 700; display: flex; align-items: center; padding-left: 8px; gap: 10px; text-decoration: none; }

  .footer-links { position: absolute; left: 10px; top: 1129px; font-size: 10px; color: var(--ink); letter-spacing: 0.3px; }
  .footer-links a { color: var(--ink); text-decoration: none; }
  .footer-bar { position: absolute; left: 0; top: 1163px; width: 748px; height: 37px; background: var(--black); color: var(--white); font-size: 10px; display: flex; align-items: center; justify-content: space-between; padding: 0 8px 0 10px; }
  .social { display: flex; gap: 4px; }
  .social span { width: 24px; height: 24px; border-radius: 3px; background: linear-gradient(#6a6a6a, #3b3b3b); border: 1px solid #888; }
</style>
</head>
<body>

<header>
  <div class="brand"><span class="brand-dot"></span><span class="brand-name">Brivol Electric</span></div>
  <div class="search">
    <span class="search-field">Search...</span>
    <span class="search-button">
      <svg width="14" height="14" viewBox="0 0 14 14"><circle cx="5.5" cy="5.5" r="4" fill="none" stroke="#555" stroke-width="1.6"/><line x1="8.5" y1="8.5" x2="13" y2="13" stroke="#555" stroke-width="2"/></svg>
    </span>
  </div>
  <nav class="main-nav">
    <a href="#" style="width:97px">Home</a>
    <a href="#" style="width:128px">About Us</a>
    <a href="#" style="width:135px">Services</a>
    <a href="#" style="width:143px">Our Work</a>
    <a href="#" style="width:132px">Specials</a>
    <a href="#" style="width:113px">Contact Us</a>
  </nav>
</header>

<section class="hero" role="img" aria-label="Slideshow photograph of high-voltage transmission towers against a pale sky">
  <svg class="hero-arrow prev" width="34" height="58" viewBox="0 0 34 58"><polygon points="34,0 14,29 34,58 20,58 0,29 20,0" fill="#9a9a9a" opacity="0.8"/></svg>
  <svg class="hero-arrow next" width="34" height="58" viewBox="0 0 34 58"><polygon points="0,0 20,29 0,58 14,58 34,29 14,0" fill="#9a9a9a" opacity="0.8"/></svg>
  <div class="hero-caption">Reduce Your Electricity Bill By<br>Lowering Your Energy Consuption</div>
</section>

<section class="promo promo-led">
  <h2 class="promo-title">LED IS THE FUTURE</h2>
  <p class="promo-text">LED lighting has involved rapidly in the last 5 years. In the coming years we will see all lighting being substituted with LED lights. It is by far the most efficient form of lighting on todays market. Let us retrofit your business or home with LED and the savings will literally pay the lights off.</p>
  <div class="promo-actions">
    <a class="btn btn-green" href="#" style="width:114px">Why Led ?</a>
    <a class="btn btn-green" href="#" style="width:114px">Request Quote</a>
  </div>
</section>

<section class="promo promo-energy">
  <h2 class="promo-title">REDUCE YOUR BUSINESS ENERGY CONSUMPTION</h2>
  <p class="promo-text">By letting us analyse your energy consumption, we can identify where you are simply burning your money. We can suggest and implement easy solutions to save you money and minimise your carbon emmissions.</p>
  <div class="promo-actions">
    <a class="btn btn-dark" href="#" style="width:154px">Energy Efficient Audit</a>
    <a class="btn btn-dark" href="#" style="width:123px;margin-left:-6px">Book Audit Now</a>
  </div>
</section>

<div class="rule" style="top:784px"></div>

<section class="service" style="left:19px">
  <h3 class="service-title">Electrical Contracting</h3>
  <div class="service-image" role="img" aria-label="Photograph of a glowing blue power button on black" style="background:radial-gradient(circle at 50% 50%, #1b5f8a 0, #0a2233 14%, #000 32%)"></div>
  <p class="service-text">Donec quam felis, ultricies nec, pellen-tesque eu, pretium quis, sem. Nulla consequat massa quis enim. Donec pede justo, fringilla vel, aliquet nec, vulputate eget, arcu.</p>
  <a class="btn-more" href="#"><svg width="10" height="11" viewBox="0 0 10 11"><polygon points="0,0 10,5.5 0,11" fill="var(--green-light)"/></svg>View More</a>
</section>

<section class="service" style="left:272px">
  <h3 class="service-title">Underground Locating</h3>
  <div class="service-image" role="img" aria-label="Photograph of a lit underground road tunnel" style="background:radial-gradient(ellipse at 50% 55%, #f2d58a 0, #9a7a3a 30%, #3a2c17 70%, #1a140b 100%)"></div>
  <p class="service-text">Donec quam felis, ultricies nec, pellen-tesque eu, pretium quis, sem. Nulla consequat massa quis enim. Donec pede justo, fringilla vel, aliquet nec, vulputate eget, arcu.</p>
  <a class="btn-more" href="#"><svg width="10" height="11" viewBox="0 0 10 11"><polygon points="0,0 10,5.5 0,11" fill="var(--green-light)"/></svg>View More</a>
</section>

<section class="service" style="left:525px">
  <h3 class="service-title">Energy Efficiency</h3>
  <div class="service-image" role="img" aria-label="Photograph of a glowing light bulb on an orange background" style="background:radial-gradient(circle at 40% 45%, #fff3b0 0, #f6b62a 35%, #e48a0c 100%)"></div>
  <p class="service-text">Donec quam felis, ultricies nec, pellen-tesque eu, pretium quis, sem. Nulla consequat massa quis enim. Donec pede justo, fringilla vel, aliquet nec, vulputate eget, arcu.</p>
  <a class="btn-more" href="#"><svg width="10" height="11" viewBox="0 0 10 11"><polygon points="0,0 10,5.5 0,11" fill="var(--green-light)"/></svg>View More</a>
</section>

<div class="rule" style="top:1111px;left:0;width:748px"></div>

<footer>
  <p class="footer-links"><a href="#">HOME</a> | <a href="#">ABOUT US</a> | <a href="#">NEWS</a> | <a href="#">BLOG</a> | <a href="#">SPECIALS</a> | <a href="#">TESTIMONIALS</a> | <a href="#">CONTACT US</a></p>
  <div class="footer-bar">
    <span>Copyright © 2013 brivolelectric.com</span>
    <div class="social"><span></span><span></span><span></span><span></span><span></span></div>
  </div>
</footer>

</body>
</html>
```